Re-brand our business and design!

We need a simple informational website (editable for in the future use)
We need our logo(we have included logo), name, who we are, and what we do displayed.

This is our current site (which is not acceptable, and only a template site): all our information is on this site, please use it forreferanceofinformation.
Www.brightlanefixers.com

Target Market(s)

Real estate brokers, and realtors,homeowners, and anyone looking for home repairs.

Industry/Entity Type

Business

Number of Pages Required

4 page

Font styles to use
Sans Serif

Requirements
Must have
• Our name, contact info, services, and our logo (which we will Email upon request)
• MUST have originality to the site.
• custom "contact us form" or request an estimate form.
Nice to have
• page for real customer testimonies.
• page for our previous work where we can upload pics of completed jobs.
Should not have
• any infringements on any copyrights or plagiarism at all.

```html
<!DOCTYPE html>
<html lang="en">
<head>
<meta charset="utf-8">
<title>Bright Lane Fixers</title>
<link href="https://fonts.googleapis.com/css2?family=Lato:wght@400;700&family=Questrial&display=swap" rel="stylesheet">
<style>
:root{
  --red:#d3171b;
  --red-dark:#a90f12;
  --ink:#222222;
  --muted:#555555;
  --light:#f4f4f4;
  --white:#ffffff;
  --cta-bg:#1b1b1b;
  --footer-bg:#2e2e2e;
  --footer-text:#e6e6e6;
  --sky-top:#3a5479;
  --sky-bottom:#8c96a5;
}
*{box-sizing:border-box;margin:0;padding:0}
html,body{width:1200px;height:2500px;overflow:hidden;background:var(--white)}
body{position:relative;font-family:'Questrial',sans-serif;color:var(--ink)}
.abs{position:absolute}

/* header */
.top-rule{left:0;top:0;width:1200px;height:5px;background:var(--red)}
.site-header{left:0;top:5px;width:1200px;height:133px;background:var(--white)}
.brand{left:52px;top:52px;display:flex;align-items:center;gap:12px}
.brand-mark{width:26px;height:26px;background:var(--red)}
.brand-name{font-family:'Lato',sans-serif;font-weight:700;font-size:25px;color:var(--ink)}
.contact-strip{top:23px;right:52px;display:flex;gap:22px;font-size:14px;color:var(--ink);align-items:center}
.contact-item{display:flex;align-items:center;gap:10px}
.icon-dot{width:22px;height:22px;border-radius:50%;background:var(--red);display:flex;align-items:center;justify-content:center}
.main-nav{top:80px;right:50px;display:flex;gap:0;font-size:16px}
.main-nav a{color:var(--ink);text-decoration:none;text-transform:uppercase;margin-left:52px}
.main-nav a.is-active{color:var(--red);text-decoration:underline;text-underline-offset:4px}

/* hero */
.hero{left:0;top:138px;width:1200px;height:592px;background:linear-gradient(180deg,var(--sky-top) 0%,#5b6f8e 45%,var(--sky-bottom) 75%,#4d5a46 100%)}
.hero-kicker{left:0;top:340px;width:1200px;text-align:center;color:var(--white);font-size:19px;letter-spacing:6px}
.hero-title{left:0;top:383px;width:1200px;text-align:center;color:var(--white);font-family:'Lato',sans-serif;font-weight:700;font-size:36px}
.hero-sub{left:0;top:443px;width:1200px;text-align:center;color:var(--white);font-size:20px}
.hero-button{left:538px;top:500px;width:124px;height:36px;border:2px solid var(--white);color:var(--white);font-size:11px;font-family:'Lato',sans-serif;font-weight:700;display:flex;align-items:center;justify-content:center}
.slider-dots{left:576px;top:685px;display:flex;gap:6px}
.slider-dots span{width:9px;height:9px;border-radius:50%;background:var(--white)}
.slider-dots span.is-open{background:transparent;border:1.5px solid var(--white)}

/* section ribbon */
.ribbon{left:0;width:253px;height:50px;background:linear-gradient(180deg,#e02a2d,var(--red-dark));clip-path:polygon(0 0,210px 0,253px 100%,0 100%);color:var(--white);font-family:'Lato',sans-serif;font-weight:700;font-size:22px;padding-left:54px;display:flex;align-items:center}

/* who we are */
.about{left:0;top:730px;width:1200px;height:457px;background:var(--light)}
.about-lead{left:53px;top:858px;width:620px;font-family:'Lato',sans-serif;font-size:14px;line-height:20px;color:var(--ink)}
.about-text{left:56px;width:610px;font-family:'Lato',sans-serif;font-size:13px;line-height:18px;color:#333}
.about-text .more{color:var(--red);font-weight:700;margin-left:8px}
.about-photo{left:728px;top:817px;width:427px;height:290px;background:#bdbdbd;padding:7px}
.about-photo div{width:100%;height:100%;background:linear-gradient(180deg,#2f3f66 0%,#55648a 50%,#d8d8d2 78%,#4f5a3b 100%)}

/* services */
.service{width:330px;text-align:center}
.service-photo{width:200px;height:200px;border-radius:50%;margin:0 auto}
.service-title{margin-top:17px;font-family:'Lato',sans-serif;font-weight:700;font-size:23px;color:var(--red-dark)}
.service-text{margin-top:16px;font-size:13px;line-height:19px;color:var(--muted)}
.service-link{margin-top:17px;font-size:16px;color:var(--red);display:flex;justify-content:center;align-items:center;gap:10px}

/* call to action */
.cta{left:0;top:1758px;width:1200px;height:272px;background:var(--cta-bg)}
.cta-title{left:0;top:1832px;width:1200px;text-align:center;color:var(--red);font-size:23px}
.cta-button{top:1918px;width:147px;height:44px;border:2px solid var(--red);color:var(--white);font-size:15px;display:flex;align-items:center;justify-content:center}

/* footer */
.site-footer{left:0;top:2030px;width:1200px;height:470px;background:var(--footer-bg)}
.footer-heading{color:var(--white);font-size:19px}
.footer-text{color:var(--footer-text);font-size:13px;line-height:21px}
.footer-line{display:flex;align-items:center;gap:14px;color:var(--footer-text);font-size:13px}
.social{left:58px;top:2317px;display:flex;gap:10px}
.social span{width:32px;height:32px;border-radius:50%}
.map{left:422px;top:2113px;width:330px;height:265px;background:linear-gradient(135deg,#e9e4d8 0%,#d8e3c8 45%,#b9d3e8 100%)}
.field{left:843px;width:280px;background:var(--white)}
.opt-in{left:848px;top:2341px;display:flex;align-items:center;gap:22px;color:var(--footer-text);font-size:11px}
.opt-in span{width:14px;height:14px;background:var(--red-dark)}
.submit{left:1040px;top:2333px;width:83px;height:32px;background:var(--red);color:var(--white);font-size:11px;display:flex;align-items:center;justify-content:center}
.footer-rule{left:0;top:2405px;width:1200px;height:1px;background:#4a4a4a}
.copyright{left:0;top:2443px;width:1200px;text-align:center;color:var(--footer-text);font-size:12px}
</style>
</head>
<body>

<div class="abs top-rule"></div>
<header class="abs site-header"></header>
<div class="abs brand"><span class="brand-mark"></span><span class="brand-name">Bright Lane Fixers</span></div>

<div class="abs contact-strip">
  <div class="contact-item">
    <span class="icon-dot"><svg width="12" height="12" viewBox="0 0 24 24"><path fill="#fff" d="M6.6 10.8c1.4 2.8 3.8 5.1 6.6 6.6l2.2-2.2c.3-.3.7-.4 1-.2 1.1.4 2.3.6 3.6.6.6 0 1 .4 1 1V20c0 .6-.4 1-1 1C10.6 21 3 13.4 3 4c0-.6.4-1 1-1h3.5c.6 0 1 .4 1 1 0 1.3.2 2.5.6 3.6.1.3 0 .7-.2 1z"/></svg></span>
    <span>555-204-7316</span>
  </div>
  <div class="contact-item">
    <span class="icon-dot"><svg width="12" height="10" viewBox="0 0 24 18"><rect x="1" y="1" width="22" height="16" fill="none" stroke="#fff" stroke-width="2"/><path d="M1 1l11 9 11-9" fill="none" stroke="#fff" stroke-width="2"/></svg></span>
    <span>Sam@brightlanefixers.com</span>
  </div>
</div>

<nav class="abs main-nav">
  <a class="is-active">Home</a><a>About Us</a><a>Services</a><a>Portfolio</a><a>Contact Us</a>
</nav>

<section class="abs hero" role="img" aria-label="Photo of a two-storey white house with grey roof at dusk, surrounded by trees"></section>
<div class="abs hero-kicker">BEYOND IMAGINATIONS</div>
<h1 class="abs hero-title">Looking for someone to help get your listing ready to show?</h1>
<div class="abs hero-sub">BRIGHT LANE FIXERS CAN HELP!</div>
<div class="abs hero-button">READ MORE</div>
<div class="abs slider-dots"><span></span><span></span><span class="is-open"></span><span></span></div>

<section class="abs about"></section>
<div class="abs ribbon" style="top:770px">Who We Are?</div>
<p class="abs about-lead">One Name, One number, One call means one service for fast timely quotes, home repairs and updates for you and/or your clients.</p>
<p class="abs about-text" style="top:922px">Looking for someone to help get your listing ready to show? A complete Home Repair Solution? Did an inspection reveal repairs needed before closing? Bright Lane Fixers can help!<br>Looking for someone to help get your listing ready to show? A complete Home Repair Solution? Did an inspection reveal repairs needed before closing? Bright Lane Fixers can help!</p>
<p class="abs about-text" style="top:1030px">Lorem Ipsum is simply dummy text of the printing and typesetting industry. Lorem Ipsum has been the industry's standard dummy text ever since the 1500s, when an unknown printer took a galley of type and scrambled it to make a type specimen book. It has survived not only five centuries, but also the leap into electronic typesetting, remaining essentially unchanged. <span class="more">Read More</span></p>
<div class="abs about-photo"><div role="img" aria-label="Photo of a lit white house with picket fence at night"></div></div>

<div class="abs ribbon" style="top:1220px">Services</div>

<div class="abs service" style="left:45px;top:1333px">
  <div class="service-photo" role="img" aria-label="Photo of stacked timber planks" style="background:radial-gradient(circle,#c49a6c,#7a5434)"></div>
  <div class="service-title">Carpentry</div>
  <p class="service-text">Lorem Ipsum is simply dummy text of the printing and typesetting industry. Lorem Ipsum has been the industry's standard dummy text ever since the 1500s</p>
  <div class="service-link">Read More <svg width="16" height="12" viewBox="0 0 16 12"><path d="M0 6h14M9 1l5 5-5 5" fill="none" stroke="#d3171b" stroke-width="1.6"/></svg></div>
</div>
<div class="abs service" style="left:432px;top:1333px">
  <div class="service-photo" role="img" aria-label="Photo of a steel double kitchen sink with tap" style="background:radial-gradient(circle at 50% 70%,#b8b8b8,#2a2a2a 70%)"></div>
  <div class="service-title">Plumbing</div>
  <p class="service-text">Lorem Ipsum is simply dummy text of the printing and typesetting industry. Lorem Ipsum has been the industry's standard dummy text ever since the 1500s</p>
  <div class="service-link">Read More <svg width="16" height="12" viewBox="0 0 16 12"><path d="M0 6h14M9 1l5 5-5 5" fill="none" stroke="#d3171b" stroke-width="1.6"/></svg></div>
</div>
<div class="abs service" style="left:818px;top:1333px">
  <div class="service-photo" role="img" aria-label="Photo of a white wall with green door and window" style="background:radial-gradient(circle,#f2f2f2,#d6d6d6)"></div>
  <div class="service-title">Doors &amp; Windows</div>
  <p class="service-text">Lorem Ipsum is simply dummy text of the printing and typesetting industry. Lorem Ipsum has been the industry's standard dummy text ever since the 1500s</p>
  <div class="service-link">Read More <svg width="16" height="12" viewBox="0 0 16 12"><path d="M0 6h14M9 1l5 5-5 5" fill="none" stroke="#d3171b" stroke-width="1.6"/></svg></div>
</div>

<section class="abs cta"></section>
<h2 class="abs cta-title">JOIN THE COMMUNITY THAT IS COMMITED TO MAKE DIFFERENCE</h2>
<div class="abs cta-button" style="left:418px">CONTACT US</div>
<div class="abs cta-button" style="left:633px">QUOTE HERE</div>

<footer class="abs site-footer"></footer>
<div class="abs footer-heading" style="left:55px;top:2065px">ADDRESS</div>
<p class="abs footer-text" style="left:55px;top:2107px;width:260px">Serving the Millbrook, and surrounding areas.</p>
<div class="abs footer-line" style="left:57px;top:2171px"><svg width="18" height="13" viewBox="0 0 24 18"><rect x="1" y="1" width="22" height="16" fill="none" stroke="#fff" stroke-width="2"/><path d="M1 1l11 9 11-9" fill="none" stroke="#fff" stroke-width="2"/></svg>Sam@brightlanefixers.com</div>
<div class="abs footer-line" style="left:57px;top:2202px"><svg width="18" height="14" viewBox="0 0 24 18"><path d="M2 6c0-4 20-4 20 0v2h-5V6H7v2H2z M5 9h14l2 8H3z" fill="#fff"/></svg>555-204-7316</div>
<div class="abs footer-line" style="left:57px;top:2233px"><svg width="18" height="15" viewBox="0 0 24 20"><rect x="6" y="0" width="12" height="6" fill="#fff"/><rect x="1" y="7" width="22" height="8" fill="#fff"/><rect x="6" y="13" width="12" height="7" fill="#fff" stroke="#2e2e2e" stroke-width="1.5"/></svg>555-204-7316</div>
<div class="abs social">
  <span style="background:#3b5998"></span><span style="background:#2ba9e1"></span><span style="background:#c13584"></span><span style="background:#cb2027"></span>
</div>

<div class="abs footer-heading" style="left:420px;top:2058px">FIND US ON MAP</div>
<div class="abs map" role="img" aria-label="Street map of the service area with a location pin"></div>

<div class="abs footer-heading" style="left:843px;top:2056px">GET QUOTE</div>
<div class="abs field" style="top:2110px;height:35px"></div>
<div class="abs field" style="top:2165px;height:35px"></div>
<div class="abs field" style="top:2217px;height:96px"></div>
<div class="abs opt-in"><span></span>receive latest news?</div>
<div class="abs submit">SUBMIT</div>

<div class="abs footer-rule"></div>
<div class="abs copyright">All Rights Reserved, Copyrights 2016</div>

</body>
</html>
```